Solar Advertising Flier to generate Biz

I need a advertisement that generates business to be used in a mailer for marketing purposes.

Im attaching a file that is a an idea of advertisement.
I do not want the "KTW" specific information on it.
I want the background solar panels.
Same information as the ad.
And I've attached my Logo - I want the color scheme to match this.

Thank you

Target Market(s)

Middle to Upper Class Home Owners

Industry/Entity Type

Solar Energy

Requirements
Must have
• A call to action
• A professional look
Nice to have
• A family
• Great looking solar panels
Should not have
• Cartoons

```html
<!DOCTYPE html>
<html lang="en">
<head>
<meta charset="utf-8">
<title>Bright Meadow Energy – Solar Mailer</title>
<link rel="stylesheet" href="https://fonts.googleapis.com/css2?family=Montserrat:wght@400;500;600;700&family=Oswald:wght@300&display=swap">
<style>
  :root {
    --navy: #12184a;
    --blue: #3391d0;
    --blue-text: #2a8ccf;
    --green: #94c83d;
    --green-text: #8cc63f;
    --orange: #f9b233;
    --sun: #fbc04a;
    --ink: #4a4a4a;
    --white: #ffffff;
  }
  * { box-sizing: border-box; margin: 0; padding: 0; }
  html, body { width: 1200px; height: 1200px; overflow: hidden; background: var(--navy); }
  body { font-family: "Montserrat", Arial, sans-serif; position: relative; }

  .flier { position: absolute; left: 34px; top: 175px; width: 1131px; height: 851px; background: var(--white); overflow: hidden; }
  .shapes { position: absolute; inset: 0; }

  .brand { position: absolute; left: 50px; top: 62px; width: 230px; text-align: center; }
  .brand-dot { width: 84px; height: 84px; border-radius: 50%; background: var(--blue); margin: 0 auto 12px; }
  .brand-name { font-weight: 600; font-size: 27px; line-height: 1.05; color: var(--blue-text); letter-spacing: 0.5px; }

  .tagline { position: absolute; left: 342px; top: 124px; display: flex; align-items: center; gap: 11px; }
  .tagline-main { font-family: "Oswald", "Arial Narrow", sans-serif; font-weight: 300; font-size: 58px; color: var(--blue-text); line-height: 1; }
  .tagline-rule { width: 2px; height: 54px; background: var(--orange); }
  .tagline-sub { font-size: 26px; color: var(--green-text); line-height: 1.05; font-weight: 500; }

  .benefits { position: absolute; left: 37px; top: 300px; list-style: none; }
  .benefit { display: flex; align-items: center; gap: 14px; height: 56px; font-size: 19px; color: var(--ink); position: relative; }
  .benefit-icon { width: 36px; height: 36px; border-radius: 50%; background: var(--green); color: var(--white); font-family: "Oswald", sans-serif; font-size: 15px; display: flex; align-items: center; justify-content: center; }
  .benefit + .benefit::before { content: ""; position: absolute; left: 50px; top: -2px; width: 178px; height: 2px; background: var(--blue); }

  .saving { position: absolute; left: 37px; top: 490px; width: 400px; color: var(--white); }
  .saving-title { font-size: 29px; font-weight: 500; }
  .saving-rule { width: 52px; height: 2px; background: var(--white); margin: 4px 0 14px; }
  .saving-body { font-size: 13.4px; line-height: 1.3; }

  .contact { position: absolute; left: 35px; top: 650px; color: var(--white); }
  .contact-lead { font-size: 13px; margin-bottom: 14px; }
  .contact-phone { display: flex; align-items: center; gap: 6px; font-size: 35px; margin-bottom: 26px; }
  .contact-line { display: flex; align-items: flex-start; gap: 10px; font-size: 18px; line-height: 1.15; margin-bottom: 6px; }
  .contact-line svg { flex: none; margin-top: 2px; }

  .cta-phone { position: absolute; left: 472px; top: 580px; display: flex; align-items: center; gap: 10px; font-size: 32px; font-weight: 700; color: var(--blue-text); }
  .cta-rule { position: absolute; left: 776px; top: 545px; width: 2px; height: 127px; background: var(--blue); opacity: .7; }
  .cta-call { position: absolute; left: 790px; top: 675px; transform: rotate(-90deg); transform-origin: left top; font-size: 26px; font-weight: 700; color: var(--blue-text); white-space: nowrap; }
  .cta-offer { position: absolute; left: 832px; top: 528px; font-weight: 700; color: var(--green-text); }
  .cta-receive { font-size: 29px; line-height: 1; }
  .cta-amount { font-size: 78px; color: var(--orange); line-height: 1; margin: 2px 0 0 -3px; letter-spacing: -1px; }
  .cta-rebate { font-size: 29px; line-height: 1; }
  .cta-rebate sup { color: var(--blue-text); font-size: 20px; }
  .fine-print { position: absolute; left: 720px; top: 702px; width: 380px; text-align: center; font-size: 10.5px; line-height: 1.25; color: var(--blue-text); }

  .scene-strip { position: absolute; left: 378px; top: 740px; width: 730px; height: 100px; }
</style>
</head>
<body>
<main class="flier">
  <svg class="shapes" width="1131" height="851" viewBox="0 0 1131 851">
    <defs>
      <linearGradient id="dusk" x1="0" y1="0" x2="0" y2="1">
        <stop offset="0" stop-color="#8f95c4"/>
        <stop offset=".45" stop-color="#b7a3b8"/>
        <stop offset=".65" stop-color="#6f7590"/>
        <stop offset=".82" stop-color="#6e8a52"/>
        <stop offset="1" stop-color="#8d91a6"/>
      </linearGradient>
      <linearGradient id="strip" x1="0" y1="0" x2="0" y2="1">
        <stop offset="0" stop-color="#ffffff" stop-opacity="0"/>
        <stop offset="1" stop-color="#e4e6ea"/>
      </linearGradient>
    </defs>
    <line x1="342" y1="112" x2="690" y2="112" stroke="var(--green)" stroke-width="2"/>
    <line x1="342" y1="202" x2="642" y2="202" stroke="var(--green)" stroke-width="2"/>
    <polygon points="726,0 1131,0 1131,474 502,474" fill="url(#dusk)" role="img" aria-label="Photo of a two-storey suburban home with rooftop solar panels at dusk"/>
    <circle cx="758" cy="6" r="56" fill="var(--sun)"/>
    <polygon points="0,254 618,254 609,274 0,274" fill="var(--blue)"/>
    <polygon points="5,474 502,474 421,622 5,622" fill="var(--green)"/>
    <polygon points="5,622 421,622 300,846 5,846" fill="var(--blue)"/>
    <line x1="726" y1="0" x2="324" y2="851" stroke="var(--orange)" stroke-width="1.5"/>
  </svg>

  <div class="brand">
    <div class="brand-dot"></div>
    <div class="brand-name">BRIGHT MEADOW ENERGY</div>
  </div>

  <div class="tagline">
    <span class="tagline-main">Switch</span>
    <span class="tagline-rule"></span>
    <span class="tagline-sub">for better,<br>to Solar.</span>
  </div>

  <ul class="benefits">
    <li class="benefit"><span class="benefit-icon">
      <svg width="18" height="18" viewBox="0 0 24 24" fill="none" stroke="#fff" stroke-width="2"><ellipse cx="12" cy="13" rx="8" ry="6"/><line x1="9" y1="19" x2="9" y2="22"/><line x1="15" y1="19" x2="15" y2="22"/></svg>
    </span>Protect yourself from rising energy costs.</li>
    <li class="benefit"><span class="benefit-icon">0$</span>$0 Down Payment, no upfront cost</li>
    <li class="benefit"><span class="benefit-icon">95%</span>Save 95% off your utility bill.</li>
  </ul>

  <section class="saving">
    <h2 class="saving-title">Start Saving Immediately.</h2>
    <div class="saving-rule"></div>
    <p class="saving-body">Your solar system allows you to generate your own<br>clean energy and costs less than the electric company.<br>Simply pay by the month, like you do now...<br>but at a lower rate.</p>
  </section>

  <section class="contact">
    <p class="contact-lead">Call Today For A No Obligation Consultation</p>
    <p class="contact-phone">
      <svg width="22" height="22" viewBox="0 0 24 24" fill="#fff"><path d="M6.6 10.8a15 15 0 0 0 6.6 6.6l2.2-2.2a1 1 0 0 1 1-.25 11.4 11.4 0 0 0 3.6.57 1 1 0 0 1 1 1V20a1 1 0 0 1-1 1A17 17 0 0 1 3 4a1 1 0 0 1 1-1h3.5a1 1 0 0 1 1 1c0 1.25.2 2.45.57 3.570a1 1 0 0 1-.25 1z"/></svg>
      (800) 555-0142
    </p>
    <p class="contact-line">
      <svg width="18" height="22" viewBox="0 0 24 30" fill="#fff"><path d="M12 0a10 10 0 0 0-10 10c0 7.5 10 20 10 20s10-12.5 10-20A10 10 0 0 0 12 0zm0 14a4 4 0 1 1 0-8 4 4 0 0 1 0 8z"/></svg>
      <span>318 Linden Ave., Suite 210-B,<br>Cedar Grove NJ 07009</span>
    </p>
    <p class="contact-line">
      <svg width="18" height="18" viewBox="0 0 24 24" fill="none" stroke="#fff" stroke-width="2"><circle cx="12" cy="12" r="10"/><ellipse cx="12" cy="12" rx="4" ry="10"/><line x1="2" y1="12" x2="22" y2="12"/></svg>
      <span>www.brightmeadow.com</span>
    </p>
  </section>

  <div class="cta-phone">
    <svg width="40" height="40" viewBox="0 0 24 24" fill="var(--orange)"><path d="M6.6 10.8a15 15 0 0 0 6.6 6.6l2.2-2.2a1 1 0 0 1 1-.25 11.4 11.4 0 0 0 3.6.57 1 1 0 0 1 1 1V20a1 1 0 0 1-1 1A17 17 0 0 1 3 4a1 1 0 0 1 1-1h3.5a1 1 0 0 1 1 1c0 1.25.2 2.45.57 3.57a1 1 0 0 1-.25 1z"/></svg>
    (800) 555-0142
  </div>
  <div class="cta-rule"></div>
  <div class="cta-call">Call Today</div>
  <div class="cta-offer">
    <div class="cta-receive">and Receive</div>
    <div class="cta-amount">$500</div>
    <div class="cta-rebate">Cash Rebate<sup>*</sup></div>
  </div>
  <p class="fine-print">*Limited time offer. This ad must be present at time of purchase.<br>Call for details. Not valid with any other offer or on previous purchases</p>

  <svg class="scene-strip" viewBox="0 0 730 100" role="img" aria-label="Light grey line illustration of wind turbines, a house, city skyline, mountains and solar panel fields">
    <rect width="730" height="100" fill="url(#strip)"/>
  </svg>
</main>
</body>
</html>
```